Northgate Prestige Academy needs a Courses Fine Brochure

An unique business school 100% focused on the luxury market that offers programs in NY, L.A., Miami, Paris, Milan, and São Paulo, needs a comprehensive brochure with all your programs.
In two versions, to print and as a web flipping book.
Please find attached two examples of our single program brochures.
PLEASE NOTE THAT ALL UPLOADED MATERIALS ARE SAMPLES OF WHAT WE ALREADY DID, AS SOON AS I´VE CHOSEN A DESIGNER I´LL SEND THE CORRECT FILES, TEXTS AND "SUGGESTED IMAGES".
Updates

Target Market(s)

US students interested in short term programs focused on luxury.
The brochure must display 12 short term programs that will take place in 2017 in Miami, Florida.

Industry/Entity Type

Education

Contact Information for Business Card

Black sober fine finishing business card.
Name, place, phone, address, e-mail, cel.

Font styles to use
Serif
Sans Serif
Script

Requirements
Must have
• Fine finishing, as smooth touch mate lamination, and/or hotstamping, and/or located varnish.
• Easy to read. Every program has Name, brief introduction, date, time, duration, some keynote speaker picture and brief resumé (short cv). And 5 to 10 content topics. Course highlights.
Nice to have
• Luxury products and services. Sofisticated images, closeups and nice views.
• We are talking about teaching luxury for entrepreneurs mainly.
• Business owners or high level executives.
Should not have
• Less is more. Promotional look. Cheap look. Colorful blasting design.

```html
<!DOCTYPE html>
<html lang="en">
<head>
<meta charset="utf-8">
<title>Hotel Architecture Summit 2017 – Brochure Spreads</title>
<link rel="stylesheet" href="https://fonts.googleapis.com/css2?family=Roboto:wght@300;400;500;700&family=Comfortaa:wght@300;400&display=swap">
<style>
  :root{
    --stage:#a3a3a3;
    --ink-dark:#231a1e;
    --ink-deep:#1a1416;
    --red:#c41f2e;
    --red-dark:#8e1522;
    --rose:#a8777b;
    --gold:#c9a14a;
    --green:#2f4a25;
    --white:#ffffff;
    --grey-page:#2b2b2d;
    --grey-light:#d9d9d9;
  }
  *{box-sizing:border-box;margin:0;padding:0}
  html,body{width:1200px;height:1074px;overflow:hidden;background:var(--stage);font-family:"Roboto",sans-serif}
  .spread{position:absolute;left:106px;width:988px;height:436px;overflow:hidden}
  .spread--cover{top:50px}
  .spread--program{top:570px}

  /* cover */
  .cover-back{position:absolute;left:0;top:0;width:494px;height:436px;background:linear-gradient(180deg,#2a2226 0%,#1e1719 60%,#241a1d 100%)}
  .cover-front{position:absolute;left:494px;top:0;width:494px;height:436px;background:linear-gradient(160deg,#6f5358 0%,#a17478 35%,#7a5a5e 60%,#3a2c2f 100%)}
  .ribbons{position:absolute;left:0;top:0}
  .brand{position:absolute;color:var(--gold);font-family:"Roboto",sans-serif;font-weight:400;font-size:17px;letter-spacing:.5px}
  .brand--back{left:32px;top:34px}
  .brand-box{position:absolute;right:22px;top:14px;width:224px;height:62px;background:rgba(60,40,44,.85);display:flex;align-items:center;justify-content:center}
  .brand--front{position:static;font-size:15px}
  .contact{position:absolute;left:30px;top:318px;list-style:none;color:#e9e3e4;font-family:"Comfortaa",sans-serif;font-weight:300;font-size:12.5px}
  .contact li{display:flex;align-items:center;height:21px}
  .contact li.gap{margin-bottom:20px}
  .contact svg{width:13px;height:13px;margin-right:16px;fill:#fff}
  .title{position:absolute;left:576px;top:294px;color:var(--white)}
  .title h1{font-weight:400;font-size:25px;line-height:30px;letter-spacing:.3px}
  .title h1 sup{font-size:13px}
  .title .city{font-size:30px;font-weight:400;line-height:40px}
  .year{position:absolute;left:808px;top:320px;color:var(--green);font-weight:700;font-size:62px;letter-spacing:1px}
  .dateline{position:absolute;left:618px;top:396px;color:#f1eaea;font-family:"Comfortaa",sans-serif;font-weight:300;font-size:15.5px}

  /* program */
  .program-left{position:absolute;left:0;top:0;width:486px;height:436px;background:linear-gradient(170deg,#3a3a3c 0%,#262628 60%,#202022 100%)}
  .hotel-photo{position:absolute;left:0;top:0;width:486px;height:150px;background:linear-gradient(180deg,#8a5d62 0%,#b48487 45%,#6b4a4c 100%)}
  .day{position:absolute;right:20px;top:116px;text-align:right;color:#fff;font-size:24px;line-height:31px;font-weight:400}
  .day .accent{color:var(--red)}
  .day-rule{position:absolute;left:270px;top:210px;width:196px;height:1px;background:#555}
  .schedule{position:absolute;top:222px;list-style:none;color:#f0f0f0;font-size:12px;line-height:18.3px}
  .schedule--am{left:26px}
  .schedule--pm{left:270px}
  .schedule .sub{color:var(--red);padding-left:44px;display:block}
  .col-rule{position:absolute;left:243px;top:222px;width:1px;height:124px;background:#6a1a22}
  .social{position:absolute;left:28px;top:368px;color:#bbb;font-size:10px;font-style:italic}
  .notes{position:absolute;left:26px;top:398px;color:#ccc;font-size:6.5px;font-style:italic;line-height:9.5px}
  .program-right{position:absolute;left:486px;top:0;width:502px;height:436px;background:#eeeeee}
  .beach-photo{position:absolute;left:16px;top:18px;width:460px;height:392px;background:linear-gradient(180deg,#d8d8d8 0%,#bdbdbd 35%,#8a8a8a 55%,#b8b8b8 75%,#e2e2e2 100%)}
  .caption{position:absolute;left:228px;top:18px;width:236px;height:106px;background:rgba(120,120,120,.72);padding:12px 20px;color:#fff}
  .caption h2{font-size:27px;font-weight:700;line-height:28px;letter-spacing:1.5px}
  .caption p{font-size:9.5px;line-height:14px;margin-top:4px}
  .top-bar{position:absolute;top:0;height:7px;background:var(--red)}
  .base-bar{position:absolute;bottom:0;height:6px;background:#bdbdbd}
</style>
</head>
<body>

<section class="spread spread--cover" aria-label="Brochure cover spread">
  <div class="cover-back" role="img" aria-label="Night photograph of a pier on dark water"></div>
  <div class="cover-front" role="img" aria-label="Rose-toned photograph of the Miami skyline and an elevated bridge at dusk"></div>

  <svg class="ribbons" width="988" height="436" viewBox="0 0 988 436">
    <g fill="none" stroke-linejoin="miter">
      <polyline points="460,-10 410,278 490,446" stroke="var(--red-dark)" stroke-width="38" opacity=".9"/>
      <polyline points="460,-10 410,278 490,446" stroke="var(--red)" stroke-width="28" opacity=".85"/>
      <polyline points="630,-10 445,446" stroke="var(--red)" stroke-width="32" opacity=".8"/>
      <polyline points="505,-10 650,150 510,340 600,446" stroke="var(--white)" stroke-width="36"/>
      <polyline points="505,-10 650,150 510,340 600,446" stroke="var(--red)" stroke-width="28"/>
    </g>
  </svg>

  <div class="brand brand--back">Northgate Prestige Academy</div>
  <div class="brand-box"><div class="brand brand--front">Northgate Prestige Academy</div></div>

  <ul class="contact">
    <li class="gap"><svg viewBox="0 0 16 16"><circle cx="8" cy="8" r="8"/><path d="M8 3.5a3 3 0 0 0-3 3c0 2.2 3 6 3 6s3-3.8 3-6a3 3 0 0 0-3-3z" fill="#231a1e"/></svg>Address goes to here.</li>
    <li><svg viewBox="0 0 16 16"><circle cx="8" cy="8" r="8"/><path d="M5 4.5l1.6-.3 1 2-1 .8a5 5 0 0 0 2.4 2.4l.8-1 2 1-.3 1.6C8 11.5 4.5 8 5 4.5z" fill="#231a1e"/></svg>0123 - 456 - 789</li>
    <li><svg viewBox="0 0 16 16"><circle cx="8" cy="8" r="8"/><rect x="4" y="5" width="8" height="6" fill="#231a1e"/><path d="M4 5l4 3 4-3" stroke="#fff" fill="none"/></svg>info#emailgoestohere.com</li>
    <li><svg viewBox="0 0 16 16"><circle cx="8" cy="8" r="8"/><circle cx="8" cy="8" r="4" fill="none" stroke="#231a1e"/><path d="M4 8h8M8 4v8" stroke="#231a1e"/></svg>www.yourwebsite.com</li>
  </ul>

  <div class="title">
    <h1>Hotel Architecture Summit <sup>®</sup></h1>
    <div class="city">Miami, Florida</div>
  </div>
  <div class="year">2017</div>
  <div class="dateline">Date goes to Here. &nbsp;| &nbsp;Venue Goes to here.</div>
</section>

<section class="spread spread--program" aria-label="Brochure program spread">
  <div class="program-left">
    <div class="hotel-photo" role="img" aria-label="Rose-toned photograph of a luxury hotel building under a dramatic sky"></div>
    <svg width="486" height="436" viewBox="0 0 486 436" style="position:absolute;left:0;top:0">
      <polygon points="0,26 135,148 486,56 486,84 135,176 0,52" fill="var(--red)"/>
      <polygon points="0,52 135,176 486,84 486,94 135,190 0,62" fill="var(--red-dark)"/>
      <line x1="0" y1="135" x2="115" y2="210" stroke="#4a4a4c" stroke-width="2"/>
      <polyline points="370,370 445,420" stroke="#4a4a4c" stroke-width="4"/>
    </svg>
    <div class="day">25/07<br><span class="accent">- A NEW LUXURY</span><br>HOSPITALITY?</div>
    <div class="day-rule"></div>
    <ul class="schedule schedule--am">
      <li>09h00 - Official Opening</li>
      <li>09h15 - Luxury Distribution<span class="sub">Special Lecture about sales</span></li>
      <li>10h30 - Coffee-break</li>
      <li>10h45 - Maison Aurelle Paris - It´s Alive!<span class="sub">Hotel Site Inspection</span></li>
      <li>12h00 - Lunch</li>
    </ul>
    <div class="col-rule"></div>
    <ul class="schedule schedule--pm">
      <li>14h00 - Le Solstice<span class="sub">Hotel Site Inspection</span></li>
      <li>15h30 - Coffee-break</li>
      <li>15h45 - Meeting Compendium<span class="sub">Panel of perceptions and<br>forecasts</span></li>
      <li>17h00 - Certificates</li>
    </ul>
    <div class="social">Social Program</div>
    <div class="notes">* Program subject to change<br>** Activities in social program are optional and charged sepparetely</div>
    <div class="base-bar" style="left:0;width:486px;background:#9a9a9a"></div>
  </div>

  <div class="program-right">
    <div class="top-bar" style="left:0;width:140px"></div>
    <div class="top-bar" style="left:146px;width:356px;background:var(--red-dark)"></div>
    <div class="beach-photo" role="img" aria-label="Black and white photograph of a beachfront with hotels and waves"></div>
    <div class="caption">
      <h2>ADD TO TEXT<br>HERE</h2>
      <p>Lorem Ipsum is simply dummy text of the printing and typesetting industry.</p>
    </div>
    <div class="base-bar" style="left:0;width:340px"></div>
    <div class="base-bar" style="left:346px;width:156px;background:#e0e0e0"></div>
  </div>
</section>

</body>
</html>
```